Financial Advisor needs a BOLD Business Card

I need a business card that is professional, and is also eye-catching and memorable. I would like to include my photo (several different professional photos have been uploaded). Preferred primary color is blue, or green, or dark purple. The final design should have a modern/contemporary look while communicating a professional image.

Target Market(s)

Individual Investors and Small Business Owners

Industry/Entity Type

Business

Contact Information for Business Card

[side 1:] Dale Varkonen Financial Advisor 58217 Marlow Brook Rd., #240 St. Louis, MO 63975 (314) 555-0187 main (314) 555-0142 cell (314) 555-0169 fax dalev@qrmvbk.com [side 2:] Life Insurance | Retirement | Employee Benefits

Font styles to use
Serif
Sans Serif

Requirements
Must have
• [disclaimer, text can be 7-9 point:] Securities offered through the K.R. Capital Trading Company. Member BLUDA/TAVK. Nine Harbor Circle, Cincinnati, Ohio 45817. 513-555-0123. Investment Advisory Services offered through K.R. Portfolio Stewardship Company.
Nice to have
• Bright, Light & Airy feel on Side 1 with contact data, bold patterns, high color contrast, modern or 3D look
Should not have
• Any symbols referring to money (e.g. $)

```html
<!DOCTYPE html>
<html lang="en">
<head>
<meta charset="utf-8">
<title>Dale Varkonen – Business Card</title>
<link rel="stylesheet" href="https://fonts.googleapis.com/css2?family=Arimo:wght@400&family=Tinos:wght@700&display=swap">
<style>
  :root {
    --bg: #e9e7e4;
    --card: #f3f3f4;
    --ink: #1c1c1c;
    --ink-soft: #6a6a6a;
    --accent: #72d0ea;
    --photo-dark: #2a2523;
    --photo-mid: #5a514b;
  }
  * { box-sizing: border-box; margin: 0; padding: 0; }
  html, body { width: 1200px; height: 914px; overflow: hidden; }
  body { background: var(--bg); font-family: "Arimo", Arial, sans-serif; color: var(--ink); position: relative; }

  .card {
    position: absolute; left: 280px; width: 640px; height: 380px;
    background: var(--card); overflow: hidden;
    box-shadow: 0 2px 8px rgba(0,0,0,0.12);
  }
  .card--back { top: 60px; }
  .card--front { top: 474px; }

  /* back side */
  .services { position: absolute; left: 220px; top: 128px; list-style: none; }
  .services li { display: flex; align-items: center; gap: 16px; font-size: 24px; line-height: 1; margin-bottom: 22px; }
  .services svg { width: 26px; height: 26px; flex: none; }

  .disclaimer {
    position: absolute; left: 40px; right: 40px; bottom: 22px;
    font-size: 9px; line-height: 1.4; color: var(--ink-soft); text-align: center;
  }

  /* front side */
  .portrait {
    position: absolute; left: 0; top: 0; width: 290px; height: 100%;
    background: radial-gradient(ellipse at 45% 55%, var(--photo-mid) 0%, var(--photo-dark) 70%);
  }
  .portrait-rule { position: absolute; left: 290px; top: 0; width: 9px; height: 100%; background: var(--accent); }

  .identity { position: absolute; left: 330px; top: 40px; }
  .name { font-family: "Tinos", "Times New Roman", serif; font-weight: 700; font-size: 31px; letter-spacing: 0.3px; }
  .title { color: var(--accent); font-size: 14px; margin-top: 2px; }

  .contacts { position: absolute; left: 330px; top: 150px; list-style: none; }
  .contacts li { display: flex; align-items: flex-start; gap: 14px; font-size: 18px; line-height: 1.2; margin-bottom: 6px; white-space: nowrap; }
  .contacts svg { width: 18px; height: 18px; flex: none; fill: var(--accent); margin-top: 2px; }
</style>
</head>
<body>

<section class="card card--back" aria-label="Card back">
  <ul class="services">
    <li><svg viewBox="0 0 26 26"><g stroke="var(--accent)" stroke-width="2" stroke-linecap="round"><line x1="13" y1="1" x2="13" y2="25"/><line x1="1" y1="13" x2="25" y2="13"/><line x1="5" y1="5" x2="21" y2="21"/><line x1="21" y1="5" x2="5" y2="21"/></g><circle cx="13" cy="13" r="4.5" fill="var(--accent)"/></svg>Life Insurance</li>
    <li><svg viewBox="0 0 26 26"><g stroke="var(--accent)" stroke-width="2" stroke-linecap="round"><line x1="13" y1="1" x2="13" y2="25"/><line x1="1" y1="13" x2="25" y2="13"/><line x1="5" y1="5" x2="21" y2="21"/><line x1="21" y1="5" x2="5" y2="21"/></g><circle cx="13" cy="13" r="4.5" fill="var(--accent)"/></svg>Retirement</li>
    <li><svg viewBox="0 0 26 26"><g stroke="var(--accent)" stroke-width="2" stroke-linecap="round"><line x1="13" y1="1" x2="13" y2="25"/><line x1="1" y1="13" x2="25" y2="13"/><line x1="5" y1="5" x2="21" y2="21"/><line x1="21" y1="5" x2="5" y2="21"/></g><circle cx="13" cy="13" r="4.5" fill="var(--accent)"/></svg>Employee Benefits</li>
  </ul>
  <p class="disclaimer">Securities offered through the K.R. Capital Trading Company. Member BLUDA/TAVK. Nine Harbor Circle, Cincinnati, Ohio 45817. 513-555-0123. Investment Advisory Services offered through K.R. Portfolio Stewardship Company.</p>
</section>

<section class="card card--front" aria-label="Card front">
  <div class="portrait" role="img" aria-label="Portrait photo of the advisor in a grey suit and light blue tie, outdoors"></div>
  <div class="portrait-rule"></div>

  <header class="identity">
    <h1 class="name">Dale Varkonen</h1>
    <p class="title">Financial Advisor</p>
  </header>

  <ul class="contacts">
    <li><svg viewBox="0 0 18 18"><path d="M1 7c0-3 4-4 8-4s8 1 8 4v1h-4V6.5c-1-.6-7-.6-8 0V8H1z"/><path d="M4 9h10l2 6H2z"/></svg>(314) 555-0187</li>
    <li><svg viewBox="0 0 18 18"><path d="M5 1h8a1 1 0 0 1 1 1v14a1 1 0 0 1-1 1H5a1 1 0 0 1-1-1V2a1 1 0 0 1 1-1zm1 2v10h6V3z"/></svg>(314) 555-0142</li>
    <li><svg viewBox="0 0 18 18"><path d="M4 1h8l2 2v4H4z"/><path d="M1 8h16v6h-3v3H4v-3H1zm5 4v3h6v-3z"/></svg>(314) 555-0169</li>
    <li><svg viewBox="0 0 18 18"><path d="M1 4h16v10H1z"/><path d="M1 4l8 6 8-6" fill="none" stroke="var(--card)" stroke-width="1.5"/></svg>dalev@qrmvbk.com</li>
    <li><svg viewBox="0 0 18 18"><path d="M9 1l8 8h-2v8h-4v-5H7v5H3V9H1z"/></svg><span>58217 Marlow Brook Rd., #240<br>St. Louis, MO 63975</span></li>
  </ul>
</section>

</body>
</html>
```